Custom Home Builder needs a Company Brochure

We need a brochure designed for our custom built building company in the Whitsundays QLD, Australia.
We are a young, fresh building company that offers clients a custom building process with outstanding quality and communication.

We would like to see designs that portray our innovative, modern culture and incorporate our company colours of bright blue, grey and white.

We don't want the brochure to be too formal, but it must flow from start to finish and be an easy to read brochure.

Our website is www.Q73bayhouses.com.au

I have other lifestyle images that I would like to add, but they are large files and I am not able to upload them to this website. I have a dropbox link with all photos https://www.crateloft.net/sh/wkt3rbn5s914mjx7/PPQvTz8_nkeRWuyLsGmRcHoLe?dl=0

I have added a photo of our work vehicle which has a style of design that I like, with the curved lines etc.

Target Market(s)

2nd and 3rd New Home owners wanting to build a quality custom designed home

Industry/Entity Type

Home Builder

Font styles to use
Sans Serif

Colors
0792cd
7f7f7f
ffffff
000000

Requirements
Must have
• A4
• Prefer portrait layout
• Creative, modern, fresh feel to the brochure
Nice to have
• I like to see soft lines rather than sharp straight lines
• Curves, waves, circles etc.

```html
<!DOCTYPE html>
<html lang="en">
<head>
<meta charset="utf-8">
<title>Q73 Bay Houses – Brochure Cover</title>
<link rel="stylesheet" href="https://fonts.googleapis.com/css2?family=Raleway:wght@400;500;600;700&display=swap">
<style>
  :root {
    --brand-blue: #0792cd;
    --sky-blue: #5db8e6;
    --pale-blue: #a9d8f2;
    --brand-grey: #7f7f7f;
    --soft-grey: #e6e7e9;
    --white: #ffffff;
    --ink: #4a4a4a;
    --backdrop: #a9a9a9;
  }
  * { box-sizing: border-box; margin: 0; padding: 0; }
  html, body { width: 1200px; height: 978px; overflow: hidden; }
  body {
    background: var(--backdrop);
    font-family: "Raleway", sans-serif;
    position: relative;
  }
  .spread {
    position: absolute;
    left: 120px; top: 149px;
    width: 960px; height: 680px;
    display: flex;
    box-shadow: 0 10px 24px rgba(0,0,0,.25);
  }
  .page { position: relative; width: 480px; height: 680px; overflow: hidden; background: var(--white); }
  .page svg.shapes { position: absolute; inset: 0; }

  .photo { position: absolute; }
  .photo--family {
    left: 0; top: 0; width: 480px; height: 418px;
    background: linear-gradient(160deg, #4f7d3c 0%, #9bb0a0 35%, #d9d2c8 60%, #6f8bbf 100%);
  }
  .photo--house {
    left: 0; top: 0; width: 480px; height: 680px;
    background: linear-gradient(180deg, #f4f5f6 0%, #e9ebec 32%, #cfcac2 45%, #b9b2a8 62%, #9a9184 74%, #6f8f45 86%, #5a7d35 100%);
  }

  .brand-name {
    position: absolute;
    font-weight: 600;
    color: var(--brand-blue);
    letter-spacing: 1px;
    white-space: nowrap;
  }
  .brand-name--back { left: 85px; top: 445px; font-size: 27px; }
  .brand-name--front { left: 70px; top: 58px; font-size: 33px; }

  .contact-list {
    position: absolute; left: 92px; top: 552px;
    list-style: none;
    font-size: 12.5px; color: var(--ink);
  }
  .contact-list li { display: flex; align-items: center; height: 20.5px; }
  .contact-list .icon { width: 13px; height: 13px; margin-right: 14px; flex: none; }

  .follow {
    position: absolute; left: 293px; top: 652px;
    display: flex; align-items: center;
    font-size: 9.5px; color: var(--ink); letter-spacing: .3px;
  }
  .follow .dot {
    width: 19px; height: 19px; border-radius: 50%;
    background: var(--brand-blue); margin-left: 8px;
  }

  .headline {
    position: absolute; left: 28px; top: 566px;
    color: var(--white);
  }
  .headline__place { font-size: 20px; font-weight: 700; letter-spacing: .3px; }
  .headline__tag { font-size: 17.5px; font-weight: 400; margin-top: 2px; }

  .web-tag {
    position: absolute; left: 238px; top: 656px;
    display: flex; align-items: center;
    color: var(--white); font-size: 13px; letter-spacing: .4px;
  }
  .web-tag svg { width: 13px; height: 13px; margin-right: 7px; }
</style>
</head>
<body>
<main class="spread">

  <!-- Back cover -->
  <section class="page page--back">
    <div class="photo photo--family" role="img" aria-label="Photo of a family sharing an outdoor barbecue lunch in a garden"></div>
    <svg class="shapes" viewBox="0 0 480 680" aria-hidden="true">
      <polygon points="225,0 480,0 480,418 275,418" fill="var(--pale-blue)" opacity=".55"/>
      <polygon points="0,418 480,418 480,680 0,680" fill="var(--white)"/>
      <polygon points="0,430 28,680 0,680" fill="var(--sky-blue)" opacity=".8"/>
      <polygon points="280,418 480,418 480,680 360,680" fill="var(--pale-blue)" opacity=".85"/>
      <polygon points="35,522 418,522 455,688 30,688" fill="var(--soft-grey)"/>
      <polygon points="135,522 418,522 440,610 180,610" fill="var(--white)" opacity=".35"/>
      <polygon points="380,550 480,550 480,612 395,612" fill="var(--brand-blue)"/>
    </svg>
    <div class="brand-name brand-name--back">Q73 BAY HOUSES</div>

    <ul class="contact-list">
      <li><svg class="icon" viewBox="0 0 14 14"><circle cx="7" cy="7" r="6.2" fill="none" stroke="var(--brand-blue)"/><path d="M7 3.5a2 2 0 0 1 2 2c0 1.5-2 4-2 4s-2-2.5-2-4a2 2 0 0 1 2-2z" fill="var(--brand-blue)"/></svg>18 Tamsin Court Bowen QLD 4805</li>
      <li><svg class="icon" viewBox="0 0 14 14"><circle cx="7" cy="7" r="6.2" fill="none" stroke="var(--brand-blue)"/><rect x="4" y="5" width="6" height="4.5" rx="1" fill="var(--brand-blue)"/></svg>0491 570 156</li>
      <li><svg class="icon" viewBox="0 0 14 14"><circle cx="7" cy="7" r="6.2" fill="none" stroke="var(--brand-blue)"/><rect x="4" y="4.8" width="6" height="4.4" fill="none" stroke="var(--brand-blue)"/><path d="M4 4.8l3 2.4 3-2.4" fill="none" stroke="var(--brand-blue)"/></svg>hello@Q73bayhouses.com.au</li>
      <li><svg class="icon" viewBox="0 0 14 14"><circle cx="7" cy="7" r="6.2" fill="none" stroke="var(--brand-blue)"/><rect x="4" y="4" width="6" height="6" fill="none" stroke="var(--brand-blue)"/><path d="M4 6h6" stroke="var(--brand-blue)"/></svg>Monday - Friday, 7am to 4pm</li>
      <li><svg class="icon" viewBox="0 0 14 14"><circle cx="7" cy="7" r="6.2" fill="none" stroke="var(--brand-blue)"/><circle cx="7" cy="7" r="3" fill="none" stroke="var(--brand-blue)"/><path d="M4 7h6" stroke="var(--brand-blue)"/></svg>www.Q73bayhouses.com.au</li>
    </ul>

    <div class="follow">FOLLOW US ON <span class="dot"></span><span class="dot"></span></div>
  </section>

  <!-- Front cover -->
  <section class="page page--front">
    <div class="photo photo--house" role="img" aria-label="Photo of a modern rendered home entrance with timber shutters and potted trees"></div>
    <svg class="shapes" viewBox="0 0 480 680" aria-hidden="true">
      <polygon points="0,30 22,30 170,680 0,680" fill="var(--brand-blue)" opacity=".35"/>
      <polygon points="0,250 60,250 175,680 0,680" fill="var(--sky-blue)" opacity=".3"/>
      <polygon points="405,0 480,0 480,340 470,340" fill="var(--brand-blue)" opacity=".5"/>
      <polygon points="0,556 380,556 368,636 0,636" fill="var(--brand-blue)"/>
      <polygon points="225,652 480,652 480,680 219,680" fill="var(--brand-blue)"/>
    </svg>
    <div class="brand-name brand-name--front">Q73 BAY HOUSES</div>

    <div class="headline">
      <div class="headline__place">Bowen &amp; Whitsunday's</div>
      <div class="headline__tag">Custom Home Building Specialist</div>
    </div>

    <div class="web-tag">
      <svg viewBox="0 0 14 14"><circle cx="7" cy="7" r="6" fill="none" stroke="#fff"/><ellipse cx="7" cy="7" rx="2.6" ry="6" fill="none" stroke="#fff"/><path d="M1 7h12" stroke="#fff"/></svg>
      www.Q73bayhouses.com.au
    </div>
  </section>

</main>
</body>
</html>
```